Tamarack Hearth Partners Business Card

Looking for a new business card layout. We are a real estate firm w/ a logo, old design attached. Must keep the same elements on there, just need a fresh look and possible some foil accents. Looking for a simpler design w/ more modern style.

Target Market(s)

Real Estate clients

Industry/Entity Type

Real Estate Agent

Contact Information for Business Card

see attached

Font styles to use
Sans Serif

Requirements
Must have
• all elements on current biz card
Nice to have
• modern look, simpler than we have!
Should not have
• no serif fonts

```html
<!DOCTYPE html>
<html lang="en">
<head>
<meta charset="utf-8">
<title>Tamarack Hearth Partners Business Card</title>
<link href="https://fonts.googleapis.com/css2?family=Poppins:wght@400;500;600&display=swap" rel="stylesheet">
<style>
  :root {
    --backdrop: #2b2b2d;
    --card-black: #050505;
    --swoosh-grey: #8e8e8e;
    --brand-grey: #8a8a8a;
    --accent-red: #d3202a;
    --text-white: #ffffff;
    --photo-light: #d9c9b0;
    --photo-mid: #b79a72;
  }
  * { margin: 0; padding: 0; box-sizing: border-box; }
  html, body {
    width: 1200px; height: 874px; overflow: hidden;
    background: var(--backdrop);
    font-family: "Poppins", sans-serif;
  }
  .stage {
    position: relative; width: 1200px; height: 874px;
    display: flex; flex-direction: column; align-items: center; justify-content: center; gap: 40px;
  }
  .card {
    position: relative; width: 560px; height: 320px;
    background: var(--card-black); border-radius: 18px; overflow: hidden;
    box-shadow: 0 14px 30px rgba(0,0,0,0.45);
  }
  .card-front { display: flex; align-items: center; justify-content: center; }
  .brand-name {
    color: var(--brand-grey); font-weight: 600; font-size: 34px;
    letter-spacing: 1px; text-transform: uppercase; text-align: center; line-height: 1.15;
  }
  .swoosh { position: absolute; inset: 0; width: 100%; height: 100%; }
  .agent-photo {
    position: absolute; left: 402px; top: 92px; width: 140px; height: 140px; border-radius: 50%;
    background: radial-gradient(circle at 50% 45%, var(--photo-light), var(--photo-mid));
    border: 4px solid var(--text-white);
  }
  .agent-info { position: absolute; left: 40px; top: 178px; color: var(--text-white); }
  .agent-name { font-weight: 600; font-size: 17px; letter-spacing: 0.5px; text-transform: uppercase; line-height: 1.1; }
  .agent-title { font-weight: 500; font-size: 10.5px; text-transform: uppercase; margin-bottom: 6px; }
  .contact-list { list-style: none; font-size: 12px; line-height: 1.45; }
  .contact-list li { display: flex; align-items: center; gap: 6px; }
  .contact-list svg { width: 11px; height: 11px; fill: var(--text-white); flex: none; }
  .contact-list .no-icon { padding-left: 17px; }
</style>
</head>
<body>
<main class="stage">
  <section class="card card-front">
    <h1 class="brand-name">Tamarack Hearth<br>Partners</h1>
  </section>

  <section class="card card-back">
    <svg class="swoosh" viewBox="0 0 560 320" aria-hidden="true">
      <path d="M0,132 C70,96 150,110 215,170 S340,300 460,320 L0,320 Z" fill="var(--accent-red)"/>
      <path d="M0,135 C70,100 150,114 213,174 S336,302 452,320 L0,320 Z" fill="var(--card-black)"/>
      <path d="M0,150 C70,116 146,130 206,188 S322,304 430,320 L0,320 Z" fill="var(--swoosh-grey)"/>
    </svg>

    <div class="agent-photo" role="img" aria-label="Portrait photo of the agent"></div>

    <div class="agent-info">
      <p class="agent-name">Marin Hale</p>
      <p class="agent-title">Principal Broker</p>
      <ul class="contact-list">
        <li><svg viewBox="0 0 24 24"><path d="M6.6 10.8a15 15 0 0 0 6.6 6.6l2.2-2.2a1 1 0 0 1 1-.25 11.4 11.4 0 0 0 3.6.57 1 1 0 0 1 1 1V20a1 1 0 0 1-1 1A17 17 0 0 1 3 4a1 1 0 0 1 1-1h3.5a1 1 0 0 1 1 1c0 1.25.2 2.45.57 3.6a1 1 0 0 1-.25 1z"/></svg>555.604.7122</li>
        <li><svg viewBox="0 0 24 24"><path d="M7 1h10a2 2 0 0 1 2 2v18a2 2 0 0 1-2 2H7a2 2 0 0 1-2-2V3a2 2 0 0 1 2-2zm0 3v14h10V4zm5 15.5a1 1 0 1 0 0 2 1 1 0 0 0 0-2z"/></svg>555.480.1208</li>
        <li><svg viewBox="0 0 24 24"><path d="M2 5h20v14H2zm2 2v.5l8 5 8-5V7zm0 2.8V17h16V9.8l-8 5z"/></svg>marin@tamarackhearth.com</li>
        <li><svg viewBox="0 0 24 24"><circle cx="12" cy="12" r="10"/></svg>TamarackHearth-Homes.com</li>
        <li class="no-icon">48 NW Birch Ave, Larkton, OR 97000</li>
      </ul>
    </div>
  </section>
</main>
</body>
</html>
```